Rack Card Design Project

We are a locally family owned public golf course. We would like to have a rack card designed that can be used for multiple applications. The colors in our logo are grey, blue, and white. Please use those in the card design. The company logo, contact information, address, and summer pricing should be included. I've included some pictures that may or may not be used. I'm also open to suggestions....use one photo, multiple photos, a stock photo or image representing golf etc.

```html
<!DOCTYPE html>
<html lang="en">
<head>
<meta charset="utf-8">
<title>Quillmont Fairways Golf Club – Summer Rates Rack Card</title>
<link href="https://fonts.googleapis.com/css2?family=Lato:wght@400;700&family=Lora:wght@700&family=Poppins:wght@600&display=swap" rel="stylesheet">
<style>
  :root {
    --navy: #12335b;
    --grey-light: #cfcfcf;
    --grey-mid: #8a8a8a;
    --grey-ring: #9a9a9a;
    --ink: #3f3f3f;
    --white: #ffffff;
    --backdrop: #e9e9e9;
  }
  * { margin: 0; padding: 0; box-sizing: border-box; }
  html, body { width: 1200px; height: 1200px; overflow: hidden; background: var(--backdrop); }
  .rack-card {
    position: absolute; left: 382px; top: 68px;
    width: 548px; height: 1330px;
    transform: scale(0.8); transform-origin: top left;
    background: var(--white); overflow: hidden;
    font-family: "Lato", sans-serif;
    box-shadow: 0 8px 22px rgba(0,0,0,0.25);
  }
  .card-art { position: absolute; left: 0; top: 0; width: 548px; height: 1330px; }
  .brand {
    position: absolute; left: 189px; top: 57px; width: 170px; height: 170px;
    border-radius: 50%; background: var(--grey-ring);
    display: flex; align-items: center; justify-content: center; text-align: center;
    color: var(--white); font-weight: 700; font-size: 19px; line-height: 1.25; padding: 18px;
  }
  .rates-title {
    position: absolute; left: 0; width: 548px; top: 643px; text-align: center;
    font-family: "Lora", serif; font-weight: 700; font-size: 53px; line-height: 64px;
    color: var(--navy); padding-left: 14px; white-space: nowrap;
  }
  .rates-season {
    position: absolute; left: 121px; top: 708px; line-height: 30px;
    font-family: "Poppins", sans-serif; font-weight: 600; font-size: 22px; letter-spacing: 0.6px; color: var(--ink);
    white-space: nowrap;
  }
  .bar {
    position: absolute; left: 70px; background: var(--navy); color: var(--white);
    display: flex; align-items: center; justify-content: center; white-space: nowrap;
  }
  .bar--header { top: 760px; width: 426px; height: 53px; font-size: 25px; }
  .bar--note { top: 1058px; width: 428px; height: 53px; font-size: 20px; }
  .rate-row { position: absolute; left: 71px; width: 422px; display: flex; gap: 7px; }
  .rate-label, .rate-price { display: flex; justify-content: center; height: 100%; white-space: nowrap; }
  .rate-label { width: 222px; background: var(--grey-light); color: var(--navy); font-size: 17px; font-weight: 700; align-items: center; }
  .rate-label--low { align-items: flex-end; padding-bottom: 7px; }
  .rate-label--high { align-items: flex-start; padding-top: 6px; }
  .rate-price { width: 193px; background: var(--grey-mid); color: var(--white); font-size: 21px; font-weight: 700; align-items: center; }
  .lunch {
    position: absolute; left: 0; width: 548px; text-align: center; color: var(--navy);
    top: 1129px; font-size: 35px; line-height: 44px; font-weight: 700; padding-left: 0; white-space: nowrap;
  }
  .lunch-hours {
    position: absolute; left: 0; width: 548px; text-align: center; color: var(--ink);
    top: 1171px; font-size: 37px; line-height: 44px; padding-left: 6px; white-space: nowrap;
  }
  .contact { position: absolute; color: var(--white); font-size: 15.5px; line-height: 20px; white-space: nowrap; }
  .contact--address { left: 74px; top: 1244px; }
  .contact--phone { left: 360px; top: 1247px; }
  .contact--web { left: 360px; top: 1282px; }
</style>
</head>
<body>
<div class="rack-card">
  <svg class="card-art" viewBox="0 0 548 1330">
    <defs>
      <linearGradient id="courseTones" x1="0" y1="0" x2="0" y2="1">
        <stop offset="0" stop-color="#dfe2e6"/>
        <stop offset="0.45" stop-color="#c4c6bd"/>
        <stop offset="0.62" stop-color="#6f7a43"/>
        <stop offset="1" stop-color="#4d7a2e"/>
      </linearGradient>
      <linearGradient id="monoTones" x1="0" y1="0" x2="0" y2="1">
        <stop offset="0" stop-color="#cfcfcf"/>
        <stop offset="0.5" stop-color="#858585"/>
        <stop offset="1" stop-color="#3b3b3b"/>
      </linearGradient>
    </defs>
    <rect class="top-band" x="0" y="0" width="548" height="660" fill="var(--navy)"/>
    <path class="course-photo" role="img" aria-label="Photo of a golf course green lined with tall pine trees at sunset" d="M0,80 Q250,-10 548,50 L548,485 Q300,540 0,448 Z" fill="url(#courseTones)"/>
    <path class="swoosh" d="M0,112 Q120,40 320,22 Q120,55 0,98 Z" fill="var(--grey-ring)"/>
    <path class="mono-photo" role="img" aria-label="Black and white photo of the golf course fairway" d="M0,455 Q300,545 548,520 L548,537 Q250,545 0,612 Z" fill="url(#monoTones)"/>
    <path class="body-white" d="M0,630 Q250,560 548,550 L548,1330 L0,1330 Z" fill="var(--white)"/>
    <path class="footer-band" d="M0,1190 Q300,1255 548,1215 L548,1330 L0,1330 Z" fill="var(--navy)"/>
    <g class="icon-pin" fill="none" stroke="#fff" stroke-width="2">
      <path d="M56,1260 C48,1250 48,1244 48,1242 A8,8 0 0 1 64,1242 C64,1244 64,1250 56,1260 Z"/>
      <circle cx="56" cy="1242" r="3"/>
      <ellipse cx="56" cy="1262" rx="9" ry="3"/>
    </g>
    <path class="icon-phone" d="M333,1251 l4,-3 l4,5 l-2,2 q2,4 6,6 l2,-2 l5,4 l-3,4 q-12,-2 -16,-16 Z" fill="#fff"/>
    <g class="icon-mail" fill="none" stroke="#fff" stroke-width="2">
      <rect x="335" y="1287" width="15" height="10"/>
      <path d="M335,1287 l7.5,6 l7.5,-6"/>
    </g>
  </svg>

  <div class="brand">Quillmont<br>Fairways<br>Golf Club</div>

  <h1 class="rates-title">SUMMER RATES</h1>
  <p class="rates-season">MAY 1 – SEPTEMBER 30</p>

  <div class="bar bar--header">18 HOLES WITH CART</div>

  <div class="rate-row" style="top:823px;height:47px"><div class="rate-label rate-label--low">7AM – 11AM $24</div><div class="rate-price">$24</div></div>
  <div class="rate-row" style="top:873px;height:48px"><div class="rate-label rate-label--low">11AM – 3PM $19</div><div class="rate-price">$19</div></div>
  <div class="rate-row" style="top:923px;height:38px"><div class="rate-label">3PM – Close $15</div><div class="rate-price">$15</div></div>
  <div class="rate-row" style="top:963px;height:42px"><div class="rate-label">9 Holes With Cart</div><div class="rate-price">$15</div></div>
  <div class="rate-row" style="top:1008px;height:40px"><div class="rate-label rate-label--high">Walking</div><div class="rate-price">$12</div></div>

  <div class="bar bar--note">Children 15 and Under Free with Paid Adult</div>

  <p class="lunch">Lunch Available Daily</p>
  <p class="lunch-hours">10AM – 3PM</p>

  <p class="contact contact--address">Quillmont Fairways Golf Club<br>412 SW Tamberlin Rd<br>Corvale, FL 34000</p>
  <p class="contact contact--phone">555-014-0278</p>
  <p class="contact contact--web">www.quillmontgc.com</p>
</div>
</body>
</html>
```